K & M Wheel Depot business cards

need business card for tire/car care company based in tampa, florida. we sell used and new tires, also we service vehicles, tune ups, oil chasnge, brakes and A/c we offer free towing with major vehicle repair and tire purchase. we also offer free estimates on any engine or a/c repair. also we have the lowest price in the city on used and new tires.

Contact Information for Business Card

4170 E Marigold Blvd,
Tampa, Fl 33581
Ph: 813-572-3186
KandMWheelDepot@Mailverse.com

Font styles to use
Serif
Sans Serif
Decorative

Requirements
Must have
• my logo, what we do ( used and new tires , oil change, brakes, tune ups, free towing vehicl. Also business info.
Nice to have
• an image of a towing truck, highlighting that we offer free towing. something close to what i have in one of the attached image

```html
<!DOCTYPE html>
<html lang="en">
<head>
<meta charset="utf-8">
<title>K &amp; M Wheel Depot — Business Cards</title>
<link href="https://fonts.googleapis.com/css2?family=Open+Sans:wght@400;600;700&display=swap" rel="stylesheet">
<style>
  :root {
    --page-bg: #ecebe8;
    --steel-light: #e4e5e7;
    --steel-mid: #b9bcc0;
    --steel-dark: #9a9da2;
    --navy: #1f3566;
    --ink: #2b2d31;
    --band: rgba(120, 124, 130, 0.35);
    --screw-ring: #7d8086;
    --screw-core: #f4f5f6;
  }
  * { box-sizing: border-box; margin: 0; padding: 0; }
  html, body {
    width: 1200px; height: 1000px; overflow: hidden;
    background: var(--page-bg);
    font-family: "Open Sans", Arial, sans-serif;
  }
  .card {
    position: absolute;
    left: 265px; width: 667px; height: 398px;
    background:
      linear-gradient(115deg, transparent 30%, rgba(255,255,255,0.55) 48%, transparent 62%),
      linear-gradient(180deg, var(--steel-light), var(--steel-mid) 55%, var(--steel-dark));
    box-shadow: 0 6px 14px rgba(0,0,0,0.25);
    overflow: hidden;
  }
  .card--front { top: 72px; }
  .card--back { top: 532px; }

  .brand {
    position: absolute;
    display: flex; align-items: center; gap: 12px;
    color: var(--navy); font-weight: 700; white-space: nowrap;
  }
  .brand__dot {
    width: 30px; height: 30px; border-radius: 50%;
    background: var(--navy); flex: none;
  }
  .card--front .brand { left: 38px; top: 168px; font-size: 28px; }
  .card--back .brand { left: 0; right: 0; justify-content: center; top: 176px; font-size: 40px; }
  .card--back .brand__dot { width: 40px; height: 40px; }

  .towing__title {
    position: absolute; left: 398px; top: 72px;
    color: var(--navy); font-weight: 700; font-size: 18px;
  }
  .towing__art {
    position: absolute; left: 398px; top: 104px; width: 192px; height: 60px;
    background: linear-gradient(90deg, #1c1d20, #3a3c42);
    border-radius: 6px;
  }
  .contact {
    position: absolute; left: 395px; right: 24px; top: 186px;
    color: var(--ink); font-size: 14px; line-height: 22px;
    white-space: nowrap;
  }
  .contact__address { margin-bottom: 8px; }
  .contact__row { display: flex; align-items: center; gap: 8px; }
  .contact__row svg { flex: none; }

  .services {
    position: absolute; left: 0; right: 0; bottom: 12px; height: 34px;
    background: var(--band);
    display: flex; align-items: center; justify-content: center;
    color: var(--navy); font-weight: 600; font-size: 14px; letter-spacing: 0.1px;
  }

  .screw {
    position: absolute; width: 28px; height: 28px; border-radius: 50%;
    background: radial-gradient(circle, var(--screw-core) 35%, var(--screw-ring) 40%, #dfe0e2 60%, #6b6e73 100%);
    box-shadow: 0 2px 3px rgba(0,0,0,0.35);
  }
  .screw--tl { left: 20px; top: 22px; }
  .screw--tr { right: 22px; top: 22px; }
  .screw--bl { left: 20px; bottom: 20px; }
  .screw--br { right: 22px; bottom: 20px; }
</style>
</head>
<body>

<section class="card card--front">
  <div class="brand"><span class="brand__dot"></span>K &amp; M Wheel Depot</div>

  <h2 class="towing__title">FREE TOWING</h2>
  <div class="towing__art" role="img" aria-label="Tow truck pulling a car"></div>

  <div class="contact">
    <p class="contact__address">4170 E Marigold Blvd,<br>Tampa, Fl 33581</p>
    <p class="contact__row">
      <svg width="13" height="13" viewBox="0 0 24 24" aria-hidden="true"><path fill="#1f3566" d="M6.6 10.8a15 15 0 0 0 6.6 6.6l2.2-2.2a1 1 0 0 1 1-.25 11.4 11.4 0 0 0 3.6.57 1 1 0 0 1 1 1V20a1 1 0 0 1-1 1A17 17 0 0 1 3 4a1 1 0 0 1 1-1h3.5a1 1 0 0 1 1 1c0 1.25.2 2.45.57 3.57a1 1 0 0 1-.25 1z"/></svg>
      813-572-3186
    </p>
    <p class="contact__row">
      <svg width="14" height="11" viewBox="0 0 14 11" aria-hidden="true"><rect width="14" height="11" rx="1" fill="#1f3566"/><path d="M1 1.5 7 6l6-4.5" stroke="#e4e5e7" stroke-width="1.2" fill="none"/></svg>
      KandMWheelDepot@Mailverse.com
    </p>
  </div>

  <div class="services">USED AND NEW TIRES , OIL CHANGE, BRAKES, TUNE UPS, FREE TOWING VEHICLE</div>
</section>

<section class="card card--back">
  <span class="screw screw--tl"></span>
  <span class="screw screw--tr"></span>
  <span class="screw screw--bl"></span>
  <span class="screw screw--br"></span>
  <div class="brand"><span class="brand__dot"></span>K &amp; M Wheel Depot</div>
</section>

</body>
</html>
```